Business Postcard Mailer - 2 sided - 6 x 10.5 inches

We will be purchasing multiple designs through this project. We need a postcard mailer for a residential painting business. The final design needs to have the special 15% Off, contact information, company logo, stamp indicia, and list of services. I will provide past examples and any additional logos. Company colors are #34482E and #4A1717. Old samples are provided. Final flat size should be 6 x 10.5 inches. And we will need a return address in the upper left-hand corner of the backside. USPS Layout Guidelines are attached. 4820 Fennel Ave #3, Waukesha, WI 53189.

I just guaranteed the project and will be expecting more entries. We will also be purchasing additional designs (4-5) so we want to ensure a good variety.

Target Market(s)

Homeowners

Industry/Entity Type

Painting

Font styles to use
Sans Serif

Requirements
Must have
• Logo and brand colors
Nice to have
• Call to action - Book your free estimate at www.BrightLoftPainting.com or Call now 262-555-0147.

```html
<!DOCTYPE html>
<html lang="en">
<head>
<meta charset="utf-8">
<title>BrightLoft Painting – Postcard Mailer</title>
<link rel="stylesheet" href="https://fonts.googleapis.com/css2?family=Montserrat:wght@400;500;600;700;800&family=Roboto:wght@400;500;700&display=swap">
<style>
  :root{
    --brand-green:#34482E;
    --logo-green:#3d5a33;
    --brand-maroon:#4A1717;
    --maroon-dark:#2a1212;
    --bar-dark:#2b2b2b;
    --ink:#1f1f1f;
    --band-grey:#e6e9e7;
    --badge-grey:#b9bfc2;
    --white:#ffffff;
  }
  *{box-sizing:border-box;margin:0;padding:0}
  html,body{width:836px;height:1200px;overflow:hidden}
  body{
    position:relative;
    background:radial-gradient(ellipse at 50% 55%,#e4e8e8 0%,#c6cccc 55%,#8f9898 100%);
    font-family:"Montserrat",Arial,sans-serif;
    color:var(--ink);
  }
  .card{position:absolute;background:var(--white);box-shadow:0 6px 14px rgba(0,0,0,.35);overflow:hidden}
  .card--front{left:38px;top:49px;width:758px;height:433px}
  .card--back{left:41px;top:565px;width:754px;height:431px}
  .card__art{position:absolute;left:0;top:0}
  .abs{position:absolute}

  .brand{position:absolute;color:var(--logo-green);font-weight:800;line-height:.95;letter-spacing:-.5px}
  .brand__name{font-size:33px;display:block}
  .brand__sub{font-size:24px;display:block;letter-spacing:1px}
  .return-address{position:absolute;font-size:9.5px;line-height:12px;font-weight:500;color:#222}

  .services{position:absolute;list-style:none;color:var(--white);font-weight:600;font-size:14px}
  .services li{display:flex;align-items:center;gap:8px;height:24.5px}
  .services svg{flex:none}

  .tagline{position:absolute;color:var(--white);font-size:12px;font-weight:500;letter-spacing:.3px}

  .offer__big{position:absolute;color:var(--brand-green);font-weight:800;letter-spacing:-1px;line-height:1}
  .offer__line1{position:absolute;font-weight:800;color:#1d1d1d;line-height:1}
  .offer__line2{position:absolute;font-weight:500;color:#1d1d1d;line-height:1}

  .cta-label{position:absolute;color:var(--white);font-weight:500;line-height:1}
  .phone{position:absolute;font-weight:800;color:#1c1c1c;line-height:1;letter-spacing:-.3px}
  .web-lead{position:absolute;color:var(--white);font-family:"Roboto",Arial,sans-serif;font-size:11.5px}
  .web-url{position:absolute;color:var(--white);font-weight:700;font-size:21px;line-height:1}
  .web-url--dark{color:#1c1c1c;font-weight:600}

  .photo-label{position:absolute;color:var(--white);font-size:10px;font-weight:700;font-family:"Roboto",Arial,sans-serif}

  .indicia{position:absolute;left:647px;top:23px;width:70px;height:70px;border:1.5px solid #111;
    font-family:"Roboto",Arial,sans-serif;font-size:8px;line-height:10px;text-align:center;padding-top:4px;color:#111}
  .indicia__paid{font-size:11px;font-weight:700;border-top:1px solid #111;border-bottom:1px solid #111;margin:3px 4px 2px;line-height:13px}
  .promise{position:absolute;left:445px;top:123px;width:272px;height:119px;border-radius:8px;background:var(--brand-green);
    color:var(--white);font-family:"Roboto",Arial,sans-serif;font-weight:500;font-size:15.5px;line-height:25px;text-align:center;
    display:flex;align-items:center;justify-content:center;padding:0 10px}
  .address-area{position:absolute;left:445px;top:254px;width:272px;height:148px;border:1px solid #c9c9c9;border-radius:8px}

  .label{position:absolute;left:0;width:836px;text-align:center;color:#222;font-weight:400}
  .label--side{font-size:36px;letter-spacing:1px}
  .label--caption{font-size:28px;line-height:40px}
</style>
</head>
<body>

<!-- FRONT -->
<section class="card card--front" aria-label="Postcard front">
  <svg class="card__art" width="758" height="433" viewBox="0 0 758 433">
    <defs>
      <linearGradient id="fServices" x1="0" y1="0" x2="1" y2="1">
        <stop offset="0" stop-color="#2a1212"/><stop offset="1" stop-color="#4A1717"/>
      </linearGradient>
      <linearGradient id="fHouse" x1="0" y1="0" x2="0" y2="1">
        <stop offset="0" stop-color="#d3d8db"/><stop offset=".55" stop-color="#8d918e"/><stop offset=".8" stop-color="#7c8a6b"/><stop offset="1" stop-color="#5e8a36"/>
      </linearGradient>
      <linearGradient id="fKitchen" x1="0" y1="0" x2="0" y2="1">
        <stop offset="0" stop-color="#d8d6d2"/><stop offset="1" stop-color="#7d7670"/>
      </linearGradient>
      <linearGradient id="fBedroom" x1="0" y1="0" x2="0" y2="1">
        <stop offset="0" stop-color="#a37a4a"/><stop offset="1" stop-color="#4a3424"/>
      </linearGradient>
      <linearGradient id="fHome2" x1="0" y1="0" x2="0" y2="1">
        <stop offset="0" stop-color="#5f8fc6"/><stop offset=".6" stop-color="#8a8f94"/><stop offset="1" stop-color="#5b7d3a"/>
      </linearGradient>
    </defs>
    <polygon points="0,104 259,104 286,238 0,238" fill="url(#fServices)"/>
    <polygon role="img" aria-label="Photo of a stone and grey-sided family home with a green lawn" points="238,0 758,0 758,238 286,238" fill="url(#fHouse)"/>
    <polygon role="img" aria-label="Photo of a bright white kitchen" points="278,247 458,247 446,354 262,354" fill="url(#fKitchen)"/>
    <polygon role="img" aria-label="Photo of a painted bedroom" points="466,247 626,247 614,354 454,354" fill="url(#fBedroom)"/>
    <polygon role="img" aria-label="Photo of a freshly painted house exterior" points="634,247 758,247 758,354 622,354" fill="url(#fHome2)"/>
    <rect x="0" y="361" width="758" height="72" fill="var(--bar-dark)"/>
    <rect x="0" y="361" width="100" height="72" fill="var(--brand-maroon)"/>
    <path d="M100,371 H322 a26,26 0 0 1 0,52 H100 L88,397 Z" fill="#fff"/>
    <circle cx="102" cy="397" r="9" fill="var(--brand-maroon)"/>
    <path d="M98.5,392.5 l2,-1 1.5,3 -1.3,1 a6,6 0 0 0 3,3 l1,-1.3 3,1.5 -1,2 c-4,0.5 -9,-4.5 -8.2,-8.2z" fill="#fff"/>
    <circle cx="377" cy="397" r="16" fill="none" stroke="#fff" stroke-width="2"/>
    <g fill="none" stroke="#fff" stroke-width="1.3">
      <circle cx="377" cy="397" r="10"/><ellipse cx="377" cy="397" rx="4.5" ry="10"/>
      <line x1="367" y1="397" x2="387" y2="397"/><line x1="369" y1="392" x2="385" y2="392"/><line x1="369" y1="402" x2="385" y2="402"/>
    </g>
  </svg>

  <div class="brand" style="left:20px;top:20px">
    <span class="brand__name">BrightLoft</span>
    <span class="brand__sub">PAINTING</span>
  </div>

  <ul class="services" style="left:26px;top:111px">
    <li><svg width="15" height="15" viewBox="0 0 16 16"><circle cx="8" cy="8" r="7" fill="none" stroke="#fff" stroke-width="1.4"/><path d="M4.8,8.2 7,10.3 11.2,5.8" fill="none" stroke="#fff" stroke-width="1.5"/></svg>Interior Painting</li>
    <li><svg width="15" height="15" viewBox="0 0 16 16"><circle cx="8" cy="8" r="7" fill="none" stroke="#fff" stroke-width="1.4"/><path d="M4.8,8.2 7,10.3 11.2,5.8" fill="none" stroke="#fff" stroke-width="1.5"/></svg>Exterior Painting</li>
    <li><svg width="15" height="15" viewBox="0 0 16 16"><circle cx="8" cy="8" r="7" fill="none" stroke="#fff" stroke-width="1.4"/><path d="M4.8,8.2 7,10.3 11.2,5.8" fill="none" stroke="#fff" stroke-width="1.5"/></svg>Carpentry Services</li>
    <li><svg width="15" height="15" viewBox="0 0 16 16"><circle cx="8" cy="8" r="7" fill="none" stroke="#fff" stroke-width="1.4"/><path d="M4.8,8.2 7,10.3 11.2,5.8" fill="none" stroke="#fff" stroke-width="1.5"/></svg>Drywall Repair</li>
    <li><svg width="15" height="15" viewBox="0 0 16 16"><circle cx="8" cy="8" r="7" fill="none" stroke="#fff" stroke-width="1.4"/><path d="M4.8,8.2 7,10.3 11.2,5.8" fill="none" stroke="#fff" stroke-width="1.5"/></svg>Color Consultations</li>
  </ul>

  <div class="tagline" style="left:531px;top:218px">LOCALLY OWNED AND OPERATED</div>

  <div class="offer__big" style="left:16px;top:258px;font-size:62px">15% OFF</div>
  <div class="offer__line1" style="left:56px;top:312px;font-size:18px">STARTING MARCH</div>
  <div class="offer__line2" style="left:56px;top:331px;font-size:16px">INTERIOR &amp; EXTERIOR</div>

  <div class="cta-label" style="left:24px;top:383px;font-size:15px">CALL<br>NOW</div>
  <div class="phone" style="left:116px;top:382px;font-size:30px">262-555-0147</div>
  <div class="web-lead" style="left:403px;top:375px">Book your free estimate at</div>
  <div class="web-url" style="left:403px;top:393px">www.BrightLoftPainting.com</div>
</section>

<div class="label label--side" style="top:503px">FRONT</div>

<!-- BACK -->
<section class="card card--back" aria-label="Postcard back">
  <svg class="card__art" width="754" height="431" viewBox="0 0 754 431">
    <defs>
      <linearGradient id="bServices" x1="0" y1="0" x2="1" y2="1">
        <stop offset="0" stop-color="#2a1212"/><stop offset="1" stop-color="#4A1717"/>
      </linearGradient>
      <linearGradient id="bBefore" x1="0" y1="0" x2="0" y2="1">
        <stop offset="0" stop-color="#5a6a50"/><stop offset=".4" stop-color="#d6d9d8"/><stop offset="1" stop-color="#9ea39c"/>
      </linearGradient>
      <linearGradient id="bAfter" x1="0" y1="0" x2="0" y2="1">
        <stop offset="0" stop-color="#d4dde4"/><stop offset=".45" stop-color="#4d5865"/><stop offset="1" stop-color="#3b4550"/>
      </linearGradient>
    </defs>
    <polygon points="0,104 245,104 226,240 0,240" fill="url(#bServices)"/>
    <polygon role="img" aria-label="Before photo: house with old white siding and ladders" points="249,0 400,0 400,118 239,118" fill="url(#bBefore)"/>
    <rect x="239" y="104" width="161" height="14" fill="rgba(0,0,0,.7)"/>
    <polygon role="img" aria-label="After photo: the same house freshly painted dark blue-grey" points="239,124 400,124 400,240 223,240" fill="url(#bAfter)"/>
    <rect x="223" y="226" width="177" height="14" fill="rgba(0,0,0,.7)"/>
    <rect x="0" y="242" width="400" height="52" fill="var(--band-grey)"/>
    <g fill="var(--badge-grey)">
      <rect x="23" y="313" width="32" height="34" rx="3"/>
      <rect x="71" y="313" width="34" height="34" rx="3"/>
      <rect x="122" y="318" width="52" height="26" rx="3"/>
      <rect x="197" y="313" width="50" height="34" rx="3"/>
      <rect x="262" y="318" width="66" height="26" rx="5"/>
      <rect x="339" y="313" width="56" height="34" rx="3"/>
    </g>
    <rect x="0" y="361" width="400" height="70" fill="var(--bar-dark)"/>
    <rect x="0" y="361" width="112" height="70" fill="var(--brand-maroon)"/>
    <path d="M112,367 H365 a18,18 0 0 1 18,18 V405 a18,18 0 0 1 -18,18 H112 L100,395 Z" fill="#fff"/>
    <circle cx="90" cy="384" r="8" fill="#fff"/>
    <path d="M87,380 l1.8,-.9 1.3,2.6 -1.1,.9 a5,5 0 0 0 2.6,2.6 l.9,-1.1 2.6,1.3 -.9,1.8 c-3.5,.4 -7.8,-3.9 -7.2,-7.2z" fill="var(--brand-maroon)"/>
    <circle cx="90" cy="405" r="8" fill="#fff"/>
    <g fill="none" stroke="var(--brand-maroon)" stroke-width="1">
      <circle cx="90" cy="405" r="5.5"/><ellipse cx="90" cy="405" rx="2.4" ry="5.5"/><line x1="84.5" y1="405" x2="95.5" y2="405"/>
    </g>
  </svg>

  <div class="brand" style="left:28px;top:16px">
    <span class="brand__name">BrightLoft</span>
    <span class="brand__sub">PAINTING</span>
  </div>
  <div class="return-address" style="left:28px;top:77px">4820 Fennel Ave #3<br>Waukesha, WI 53189</div>

  <div class="photo-label" style="left:302px;top:104px">Before</div>
  <div class="photo-label" style="left:308px;top:226px">After</div>

  <ul class="services" style="left:26px;top:112px">
    <li><svg width="15" height="15" viewBox="0 0 16 16"><circle cx="8" cy="8" r="7" fill="none" stroke="#fff" stroke-width="1.4"/><path d="M4.8,8.2 7,10.3 11.2,5.8" fill="none" stroke="#fff" stroke-width="1.5"/></svg>Interior Painting</li>
    <li><svg width="15" height="15" viewBox="0 0 16 16"><circle cx="8" cy="8" r="7" fill="none" stroke="#fff" stroke-width="1.4"/><path d="M4.8,8.2 7,10.3 11.2,5.8" fill="none" stroke="#fff" stroke-width="1.5"/></svg>Exterior Painting</li>
    <li><svg width="15" height="15" viewBox="0 0 16 16"><circle cx="8" cy="8" r="7" fill="none" stroke="#fff" stroke-width="1.4"/><path d="M4.8,8.2 7,10.3 11.2,5.8" fill="none" stroke="#fff" stroke-width="1.5"/></svg>Carpentry Services</li>
    <li><svg width="15" height="15" viewBox="0 0 16 16"><circle cx="8" cy="8" r="7" fill="none" stroke="#fff" stroke-width="1.4"/><path d="M4.8,8.2 7,10.3 11.2,5.8" fill="none" stroke="#fff" stroke-width="1.5"/></svg>Drywall Repair</li>
    <li><svg width="15" height="15" viewBox="0 0 16 16"><circle cx="8" cy="8" r="7" fill="none" stroke="#fff" stroke-width="1.4"/><path d="M4.8,8.2 7,10.3 11.2,5.8" fill="none" stroke="#fff" stroke-width="1.5"/></svg>Color Consultations</li>
  </ul>

  <div class="offer__big" style="left:19px;top:249px;font-size:42px">15% OFF</div>
  <div class="offer__line1" style="left:209px;top:252px;font-size:16.5px">STARTING MARCH</div>
  <div class="offer__line2" style="left:209px;top:270px;font-size:14.5px">INTERIOR &amp; EXTERIOR</div>

  <div class="cta-label" style="left:21px;top:384px;font-size:9px;line-height:13px;font-weight:600;text-align:center">Call now or<br>Book Now</div>
  <div class="phone" style="left:124px;top:370px;font-size:29px">262-555-0147</div>
  <div class="web-url web-url--dark" style="left:124px;top:402px;font-size:15.5px">www.BrightLoftPainting.com</div>

  <div class="indicia">Presorted<br>Standard<br>U.S. Postage<div class="indicia__paid">PAID</div>RMS</div>
  <div class="promise">We cater the size of the crew to the size of the job and work full continuous days until the project is complete.</div>
  <div class="address-area" aria-label="Mailing address area"></div>
</section>

<div class="label label--side" style="top:1028px">BACK</div>
<div class="label label--caption" style="top:1094px">Business Postcard Mailer - 2 sided<br>6 x 10.5 inches</div>

</body>
</html>
```